Awesome photographers card for an awesome new business

Double sided business card Black background and silver logo in middle on one side. Details on otherside. please keep it simple

Photographer

Gavin Tolley
0482615073
GavinTolleyPhotography82@lumenpost.com
www.GavinTolleyPhotography.com.au
Instagram _Gavin_tolley

Requirements
Must have
• My logo in Silver
• please use instagram logo instead of "Instagram"

```html
<!DOCTYPE html>
<html lang="en">
<head>
<meta charset="utf-8">
<title>Gavin Tolley Photography – Business Card</title>
<link rel="stylesheet" href="https://fonts.googleapis.com/css2?family=Lato:wght@400;700&display=swap">
<style>
  :root {
    --stage: #2a2a2a;
    --card-front: #161616;
    --card-front-edge: #262626;
    --card-back: #ffffff;
    --silver: #cfcfcf;
    --ink: #666666;
    --ink-soft: #707070;
  }
  html, body {
    margin: 0;
    width: 1200px;
    height: 897px;
    overflow: hidden;
    background: var(--stage);
    font-family: "Lato", sans-serif;
  }
  .canvas {
    position: relative;
    width: 1200px;
    height: 897px;
  }
  .card {
    position: absolute;
    left: 350px;
    width: 490px;
    height: 278px;
    box-sizing: border-box;
  }
  .card--front {
    top: 160px;
    background: radial-gradient(circle at 80% 40%, var(--card-front-edge), var(--card-front) 70%);
  }
  .card--back {
    top: 468px;
    left: 348px;
    width: 492px;
    background: var(--card-back);
  }
  .brand-mark {
    position: absolute;
    left: 50%;
    top: 50%;
    width: 172px;
    height: 172px;
    transform: translate(-50%, -50%);
  }
  .brand-mark__ring {
    position: absolute;
    inset: 0;
    border: 2px solid var(--silver);
    border-radius: 50%;
  }
  .brand-mark__name {
    position: absolute;
    inset: 0;
    display: flex;
    align-items: center;
    justify-content: center;
    color: var(--silver);
    font-size: 15px;
    font-weight: 400;
    letter-spacing: 0.22em;
    text-align: center;
    line-height: 1.6;
  }
  .details__name {
    position: absolute;
    left: 32px;
    top: 108px;
    margin: 0;
    font-size: 13px;
    line-height: 16px;
    font-weight: 400;
    letter-spacing: 0.26em;
    color: var(--ink);
    text-transform: uppercase;
  }
  .details__rule {
    position: absolute;
    left: 34px;
    top: 168px;
    width: 42px;
    height: 0;
    border-top: 1px solid var(--ink-soft);
  }
  .details__contact {
    position: absolute;
    left: 34px;
    top: 210px;
    margin: 0;
    font-size: 11.5px;
    line-height: 20px;
    letter-spacing: 0.04em;
    color: var(--ink-soft);
    white-space: nowrap;
  }
</style>
</head>
<body>
  <main class="canvas">
    <section class="card card--front" aria-label="Card front">
      <div class="brand-mark">
        <div class="brand-mark__ring"></div>
        <div class="brand-mark__name">GAVIN<br>TOLLEY</div>
      </div>
    </section>

    <section class="card card--back" aria-label="Card back">
      <h1 class="details__name">Gavin Tolley</h1>
      <div class="details__rule"></div>
      <p class="details__contact">
        0482615073 | GavinTolleyPhotography82@lumenpost.com<br>
        Ins: _Gavin_tolley | www.GavinTolleyPhotography.com.au
      </p>
    </section>
  </main>
</body>
</html>
```